Website design and coding for new consultancy company

I need to have a full website designed for a new consultancy business I'm trying to establish. It's called Brightpath consult. I need an English version to begin with, and then there should be a Danish version as well, but I'll translate that myself. Just be aware that I need two language versions. The consultancy field that I'm targeting is Leadership - and specialist development. I offer to facilitate corporate academies for global companies as well as specific workshops within leadership- or team development, strategy sessions, personal coaching and facilitation of D&I (Diversity and inclusion) workshops. BTW my logo is not in high resolution - I need that as well.

Target Market(s)

Larger companies that has a need for developing their inhouse leadership capabilities or that wants to develop their specialists to take on more responsibility.

Industry/Entity Type

Consultancy business

Coding

Number of Pages Required

5+ page

Requirements
Must have
• Introduction site with a catch phrase. Book a meeting. Services that's beeing offered. Blog site with white papers etc. Language toggle (Danish/English). Cases/testimonials. About site. Contact site.

```html
<!DOCTYPE html>
<html lang="en">
<head>
<meta charset="utf-8">
<title>Brightpath consult</title>
<link href="https://fonts.googleapis.com/css2?family=Saira+Condensed:wght@600;700;800&family=Poppins:wght@400;500;600&display=swap" rel="stylesheet">
<style>
  :root{
    --blue:#2a7cc6;
    --blue-deep:#1c64a8;
    --blue-light:#cfe3f4;
    --blue-pale:#eaf3fb;
    --ink:#141414;
    --muted:#555;
    --white:#fff;
    --head:"Saira Condensed", "Arial Narrow", sans-serif;
    --body:"Poppins", Arial, sans-serif;
  }
  *{margin:0;padding:0;box-sizing:border-box}
  html,body{width:1200px;height:4412px;overflow:hidden;background:var(--white)}
  body{position:relative;font-family:var(--body);color:var(--ink)}
  .layer{position:absolute;left:0;top:0;width:1200px;height:4412px}
  .abs{position:absolute}
  h1,h2,h3,h4{font-family:var(--head);font-weight:800;text-transform:uppercase;line-height:.95}
  .btn{position:absolute;display:inline-block;background:var(--blue);color:var(--white);font-family:var(--body);font-size:11px;font-weight:600;letter-spacing:.5px;text-transform:uppercase;padding:13px 26px;border-radius:2px}

  /* header */
  .brand{left:100px;top:26px;display:flex;align-items:center;gap:10px}
  .brand-mark{width:14px;height:14px;background:var(--blue)}
  .brand-name{font-family:var(--head);font-weight:800;font-size:40px;color:var(--blue-deep);letter-spacing:1px}
  .nav{left:486px;top:46px;display:flex;gap:18px;font-size:11px;font-weight:600}
  .nav .active{color:var(--blue)}
  .lang{left:1016px;top:38px;display:flex;align-items:center;gap:6px;background:var(--white);border:1px solid #ddd;border-radius:14px;padding:5px 10px;font-size:10px;font-weight:600}
  .lang-dot{width:12px;height:12px;border-radius:50%;background:#c8102e}

  /* hero */
  .hero-title{left:100px;top:172px;font-size:68px;width:600px}
  .hero-text{left:100px;top:332px;width:380px;font-size:13px;line-height:1.55;color:var(--muted)}
  .hero-btn{left:100px;top:400px}

  /* about */
  .about-title{left:0;width:1200px;top:596px;text-align:center;font-size:54px;color:var(--white)}
  .about-lead{left:0;width:1200px;top:660px;text-align:center;font-size:12px;color:var(--white)}
  .point{left:650px;width:480px;color:var(--white)}
  .point h3{font-size:26px;display:flex;align-items:center;gap:12px;margin-bottom:12px}
  .point p{font-size:12px;line-height:1.6;padding-left:36px}

  /* services */
  .section-title{left:0;width:1200px;text-align:center;font-size:52px}
  .service{width:210px;text-align:center}
  .service svg{display:block;margin:0 auto 16px}
  .service h4{font-size:18px;margin-bottom:8px}
  .service p{font-size:11px;line-height:1.55;color:var(--muted)}

  /* why */
  .why-title{left:100px;top:1938px;font-size:54px}
  .reason{left:110px;display:flex;gap:18px;align-items:flex-start}
  .reason h4{font-size:19px;margin-bottom:4px}
  .reason p{font-size:11px;color:var(--muted)}

  /* testimonials */
  .testi-title{left:0;width:1200px;top:2510px;text-align:center;font-size:46px;color:var(--blue-light)}
  .quote{left:560px;top:2608px;width:420px;color:var(--white)}
  .quote p{font-size:15px;line-height:1.6;padding-bottom:22px;border-bottom:1px solid rgba(255,255,255,.6);margin-bottom:18px}
  .quote strong{display:block;font-family:var(--head);font-size:20px;text-transform:uppercase}
  .quote span{font-size:11px}
  .dots{display:flex;gap:8px}
  .dots i{width:8px;height:8px;border-radius:50%;background:rgba(255,255,255,.5)}
  .dots i.on{background:var(--white)}
  .dots.dark i{background:#c7c7c7}
  .dots.dark i.on{background:#333}

  /* blog */
  .card{top:3084px;width:286px;height:430px;background:var(--white);box-shadow:0 6px 22px rgba(0,0,0,.1)}
  .card-img{width:286px;height:236px}
  .card-body{padding:18px 20px}
  .card-body h4{font-size:21px;margin-bottom:12px}
  .card-date{display:flex;align-items:center;gap:6px;font-size:10px;color:var(--muted);margin-bottom:12px}
  .card-body p{font-size:11px;line-height:1.55;color:var(--muted)}

  /* cta */
  .cta-title{left:540px;top:3540px;font-size:58px;width:600px}
  .cta-btn{left:612px;top:3734px}

  /* footer */
  .foot-brand{left:0;width:1200px;top:4120px;text-align:center;color:var(--white)}
  .foot-brand .name{font-family:var(--head);font-weight:800;font-size:72px;letter-spacing:2px}
  .foot-brand .tag{font-size:11px;letter-spacing:4px;text-transform:uppercase}
  .copy{left:0;width:1200px;top:4374px;text-align:center;color:var(--white);font-size:10px;text-transform:uppercase;letter-spacing:.5px}
</style>
</head>
<body>

<svg class="layer" viewBox="0 0 1200 4412" aria-hidden="true">
  <defs>
    <linearGradient id="bandBlue" x1="0" y1="0" x2="1" y2="1">
      <stop offset="0" stop-color="#5aa3de"/><stop offset="1" stop-color="#1f6fb8"/>
    </linearGradient>
    <linearGradient id="paleFade" x1="0" y1="0" x2="1" y2="0">
      <stop offset="0" stop-color="#eaf3fb" stop-opacity="0"/><stop offset="1" stop-color="#d5e7f6"/>
    </linearGradient>
    <linearGradient id="footBlue" x1="0" y1="0" x2="0" y2="1">
      <stop offset="0" stop-color="#4a96d6"/><stop offset="1" stop-color="#1c64a8"/>
    </linearGradient>
  </defs>
  <!-- hero wash -->
  <polygon points="0,0 1200,0 1200,520 0,760" fill="url(#paleFade)"/>
  <!-- about band -->
  <polygon points="0,560 1200,480 1200,1260 0,1330" fill="url(#bandBlue)"/>
  <polygon points="0,520 1200,440 1200,480 0,560" fill="#cfe3f4"/>
  <!-- why choose decoration -->
  <polygon points="600,2440 1200,1860 1200,2440" fill="#eaf3fb"/>
  <!-- testimonials band -->
  <polygon points="0,2470 1200,2420 1200,2860 0,2920" fill="url(#bandBlue)"/>
  <!-- footer -->
  <polygon points="0,4060 1200,3940 1200,4412 0,4412" fill="url(#footBlue)"/>
  <polygon points="1070,4320 1100,4270 1130,4320" fill="#bcd8f1"/>
</svg>

<!-- header -->
<div class="abs brand"><span class="brand-mark"></span><span class="brand-name">BRIGHTPATH</span></div>
<nav class="abs nav"><span class="active">HOME</span><span>ABOUT</span><span>SERVICE</span><span>CONTACT</span></nav>
<div class="abs lang"><span class="lang-dot"></span>ENG ▾</div>

<!-- hero -->
<h1 class="abs hero-title">Management that works in practice</h1>
<p class="abs hero-text">I help specialists and managers take even more responsibility, set clear direction and create effective collaborations.</p>
<a class="btn hero-btn">Book a meeting</a>
<svg class="abs" style="left:640px;top:60px" width="560" height="640" viewBox="0 0 560 640">
  <polygon points="20,20 550,20 285,630" fill="var(--blue)"/>
  <polygon points="40,36 530,36 285,590" fill="#fff"/>
  <polygon points="56,48 514,48 285,560" fill="#9fb6c8" role="img" aria-label="Portrait photo of the consultant in a suit"/>
</svg>

<!-- about -->
<h2 class="abs about-title">About Brightpath</h2>
<p class="abs about-lead">Leadership is not about titles – it is about taking responsibility for the business, cooperation and development</p>
<svg class="abs" style="left:70px;top:690px" width="540" height="520" viewBox="0 0 540 520">
  <polygon points="270,0 540,510 0,510" fill="#fff"/>
  <polygon points="270,24 512,494 28,494" fill="#8a9fb0" role="img" aria-label="Photo of a facilitator presenting to a team in a meeting room"/>
</svg>
<div class="abs point" style="top:820px">
  <h3><svg width="24" height="22"><polygon points="12,2 22,20 2,20" fill="none" stroke="#fff" stroke-width="2"/></svg>Purpose of Brightpath</h3>
  <p>I help organisations get the full potential out of their leaders and specialists by building clarity, ownership and trust, so teams can act with purpose and grow in a way that lasts.</p>
</div>
<div class="abs point" style="top:990px">
  <h3><svg width="24" height="22"><polygon points="12,2 22,20 2,20" fill="none" stroke="#fff" stroke-width="2"/></svg>Specialists with increased responsibility</h3>
  <p>Many companies find it hard to give specialists more responsibility. I support them with practical tools, clear roles and guidance so they can lead projects, people and decisions with confidence.</p>
</div>

<!-- services -->
<h2 class="abs section-title" style="top:1384px">Our Brightpath Services</h2>
<div class="abs service" style="left:155px;top:1460px">
  <svg width="120" height="104" viewBox="0 0 120 104"><polygon points="60,4 116,100 4,100" fill="none" stroke="var(--blue)" stroke-width="4"/><polygon points="60,48 84,58 60,68 36,58" fill="none" stroke="#111" stroke-width="3"/><path d="M46 63v10c8 6 20 6 28 0V63" fill="none" stroke="#111" stroke-width="3"/></svg>
  <h4>Corporate Academies</h4>
  <p>Tailored learning programs that build long-term leadership and specialist capabilities across your organisation.</p>
</div>
<div class="abs service" style="left:375px;top:1460px">
  <svg width="120" height="104" viewBox="0 0 120 104"><polygon points="60,4 116,100 4,100" fill="none" stroke="var(--blue)" stroke-width="4"/><circle cx="60" cy="56" r="7" fill="none" stroke="#111" stroke-width="3"/><circle cx="42" cy="64" r="5" fill="none" stroke="#111" stroke-width="3"/><circle cx="78" cy="64" r="5" fill="none" stroke="#111" stroke-width="3"/><path d="M46 84c2-10 26-10 28 0M32 84c1-7 12-8 16-5M88 84c-1-7-12-8-16-5" fill="none" stroke="#111" stroke-width="3"/></svg>
  <h4>Leadership &amp; Team</h4>
  <p>Practical, engaging sessions to strengthen leadership skills, teamwork, and cross-functional collaboration.</p>
</div>
<div class="abs service" style="left:595px;top:1460px">
  <svg width="120" height="104" viewBox="0 0 120 104"><polygon points="60,4 116,100 4,100" fill="none" stroke="var(--blue)" stroke-width="4"/><circle cx="60" cy="68" r="16" fill="none" stroke="#111" stroke-width="3"/><circle cx="60" cy="68" r="7" fill="none" stroke="#111" stroke-width="3"/><path d="M60 68l16-16m0 0h-6m6 0v6" fill="none" stroke="#111" stroke-width="3"/></svg>
  <h4>Strategy Sessions</h4>
  <p>Facilitation of executive and team strategy workshops, creating clarity and alignment on key goals.</p>
</div>
<div class="abs service" style="left:835px;top:1460px">
  <svg width="120" height="104" viewBox="0 0 120 104"><polygon points="60,4 116,100 4,100" fill="none" stroke="var(--blue)" stroke-width="4"/><circle cx="60" cy="56" r="9" fill="none" stroke="#111" stroke-width="3"/><path d="M42 88c2-16 34-16 36 0" fill="none" stroke="#111" stroke-width="3"/></svg>
  <h4>Personal Coaching</h4>
  <p>One-on-one coaching to support leaders in building resilience, confidence, and effective decision-making.</p>
</div>
<a class="btn" style="left:528px;top:1686px">Explore all services</a>

<!-- why choose -->
<h2 class="abs why-title">Why choose Brightpath?</h2>
<div class="abs reason" style="top:2012px"><svg width="26" height="24"><polygon points="13,2 24,22 2,22" fill="none" stroke="var(--blue)" stroke-width="2"/></svg><div><h4>Global Perspective</h4><p>Experience facilitating programs for international companies.</p></div></div>
<div class="abs reason" style="top:2080px"><svg width="26" height="24"><polygon points="13,2 24,22 2,22" fill="none" stroke="var(--blue)" stroke-width="2"/></svg><div><h4>Practical Impact</h4><p>Focus on leadership that drives real-world results.</p></div></div>
<div class="abs reason" style="top:2148px"><svg width="26" height="24"><polygon points="13,2 24,22 2,22" fill="none" stroke="var(--blue)" stroke-width="2"/></svg><div><h4>Customized Approach</h4><p>Tailored solutions to fit your company's culture and goals.</p></div></div>
<div class="abs reason" style="top:2216px"><svg width="26" height="24"><polygon points="13,2 24,22 2,22" fill="none" stroke="var(--blue)" stroke-width="2"/></svg><div><h4>Sustainable Change</h4><p>Building capacity that lasts beyond the workshop.</p></div></div>
<svg class="abs" style="left:660px;top:1870px" width="540" height="540" viewBox="0 0 540 540">
  <polygon points="290,10 540,520 40,520" fill="var(--blue)"/>
  <polygon points="270,0 520,500 20,500" fill="#dbe8f3"/>
  <polygon points="270,30 496,488 44,488" fill="#a8b8c5" role="img" aria-label="Portrait photo of the consultant smiling"/>
</svg>

<!-- testimonials -->
<h2 class="abs testi-title">Client's Testimonials</h2>
<svg class="abs" style="left:250px;top:2590px" width="220" height="180" viewBox="0 0 220 180" aria-hidden="true">
  <path d="M10 170V90C10 40 40 12 92 6v30C62 44 54 62 54 84h38v86z" fill="#fff"/>
  <path d="M120 170V90c0-50 30-78 82-84v30c-30 8-38 26-38 48h38v86z" fill="#fff"/>
</svg>
<div class="abs quote">
  <p>"Brightpath helped us align our leadership team and strengthen collaboration across regions."</p>
  <strong>— Global HR Director</strong>
  <span>Fortune 500 company</span>
</div>
<div class="abs dots" style="left:576px;top:2806px"><i class="on"></i><i></i><i></i></div>

<!-- blog -->
<h2 class="abs section-title" style="top:3004px">Latest Blog Post</h2>
<article class="abs card" style="left:148px">
  <div class="card-img" style="background:linear-gradient(135deg,#c9d3dc,#7d8e9c)" role="img" aria-label="Photo of a team meeting around a table"></div>
  <div class="card-body"><h4>Some blog heading goes here with des...</h4><div class="card-date"><svg width="12" height="12"><rect x="1" y="2" width="10" height="9" fill="none" stroke="#2a7cc6"/></svg>12 MARCH 2025</div><p>Aenean lorem ipsum bibendum auctor, nisi elit consequat ipsum.</p></div>
</article>
<article class="abs card" style="left:457px">
  <div class="card-img" style="background:linear-gradient(135deg,#d8d2c8,#8b8478)" role="img" aria-label="Photo of colleagues discussing at a desk"></div>
  <div class="card-body"><h4>Some blog heading goes here with des...</h4><div class="card-date"><svg width="12" height="12"><rect x="1" y="2" width="10" height="9" fill="none" stroke="#2a7cc6"/></svg>12 MARCH 2025</div><p>Aenean lorem ipsum bibendum auctor, nisi elit consequat ipsum.</p></div>
</article>
<article class="abs card" style="left:766px">
  <div class="card-img" style="background:linear-gradient(135deg,#d9c6ad,#7a6148)" role="img" aria-label="Photo of a smiling professional in an office"></div>
  <div class="card-body"><h4>Some blog heading goes here with des...</h4><div class="card-date"><svg width="12" height="12"><rect x="1" y="2" width="10" height="9" fill="none" stroke="#2a7cc6"/></svg>12 MARCH 2025</div><p>Aenean lorem ipsum bibendum auctor, nisi elit consequat ipsum.</p></div>
</article>
<div class="abs dots dark" style="left:576px;top:3560px"><i class="on"></i><i></i><i></i></div>

<!-- cta -->
<svg class="abs" style="left:60px;top:3590px" width="420" height="480" viewBox="0 0 420 480" aria-hidden="true">
  <defs><linearGradient id="ctaTri" x1="0" y1="0" x2="0" y2="1"><stop offset="0" stop-color="#eaf3fb"/><stop offset="1" stop-color="#7db5e3"/></linearGradient></defs>
  <polygon points="200,0 400,460 0,460" fill="url(#ctaTri)" stroke="#cfe3f4" stroke-width="6"/>
</svg>
<h2 class="abs cta-title">Ready to strengthen your leadership and teams?</h2>
<a class="btn cta-btn">Book a meeting today</a>

<!-- footer -->
<div class="abs foot-brand"><div class="name">BRIGHTPATH</div><div class="tag">Inspiring performance</div></div>
<p class="abs copy">© Copyright Brightpath consult. All rights reserved</p>

</body>
</html>
```